Home page graphic design only (NOT WEBSITE DESIGN)

I require a home page to be designed for my new website.
I DO NOT REQUIRE to build a website. We are a rug company specialising in alpaca wool. It is targeted at the high end of the market and hence the graphics of our page requires to reflect this. Our current page is as per attachment and I think it is too basic.
Updates

Target Market(s)

Extremly high net worth individuals where luxury is a requirement

Requirements
Must have
• show of style, luxury, uniqueness. Prefer having bright images.
Nice to have
• a highly sofisticated roomscape where the focus in the rug. See attachment as an example
Should not have
• Not sure

```html
<!DOCTYPE html>
<html lang="en">
<head>
<meta charset="utf-8">
<title>Maison Velours — Luxury Alpaca Rugs</title>
<link rel="stylesheet" href="https://fonts.googleapis.com/css2?family=Prata&family=Rozha+One&family=Yesteryear&family=Outfit:wght@400;600&display=swap">
<style>
  :root{
    --black:#000;
    --gold-text:#d9b45a;
    --cream:#ffdc7e;
    --cream-light:#ffe08a;
    --brown:#3a2806;
    --script:#a87a0c;
    --band-gold:#c48e00;
    --band-dark:#2e2208;
    --band-yellow:#f7b900;
    --white:#fff;
  }
  *{margin:0;padding:0;box-sizing:border-box}
  html,body{width:1200px;height:834px;overflow:hidden;background:var(--black)}
  .page{position:relative;width:1200px;height:834px;overflow:hidden}

  .site-header{position:absolute;top:0;left:0;width:1200px;height:81px;background:var(--black);display:flex;align-items:center}
  .brand{position:absolute;left:55px;top:20px;font-family:"Prata",serif;font-size:30px;color:var(--gold-text);letter-spacing:1px;white-space:nowrap}
  .main-nav{position:absolute;left:464px;top:33px;display:flex;gap:15.5px;font-family:"Outfit",sans-serif;font-size:12px;color:var(--white);white-space:nowrap}
  .main-nav .caret{display:inline-block;margin-left:5px;border-left:3.5px solid transparent;border-right:3.5px solid transparent;border-top:4px solid var(--white);vertical-align:middle}
  .header-tools{position:absolute;left:1066px;top:30px;width:110px;height:24px}
  .header-tools svg{position:absolute}
  .cart-count{position:absolute;left:88px;top:-6px;font-family:"Outfit",sans-serif;font-size:11px;color:var(--white)}

  .hero{position:absolute;top:81px;left:0;width:1200px;height:659px}
  .hero svg{position:absolute;inset:0}
  .hero-copy{position:absolute;left:53px;top:255px;color:var(--brown)}
  .hero-line{display:block;white-space:nowrap;line-height:48px}
  .serif-light{font-family:"Prata",serif;font-size:31px}
  .serif-bold{font-family:"Rozha One",serif;font-size:46px}
  .hero-script{display:block;margin-top:12px;margin-left:10px;font-family:"Yesteryear",cursive;font-size:70px;color:var(--script);white-space:nowrap}

  .reach-band{position:absolute;top:740px;left:0;width:1200px;height:94px;background:var(--band-gold)}
  .reach-band svg{position:absolute;inset:0}
  .established,.abn{position:absolute;top:32px;font-family:"Outfit",sans-serif;font-style:italic;font-size:19px;color:var(--white);white-space:nowrap}
  .established{left:71px}
  .abn{left:967px;top:34px}
  .regions{position:absolute;left:299px;width:620px;top:29px;text-align:center;font-family:"Outfit",sans-serif;font-weight:600;font-size:24px;color:var(--band-yellow);white-space:nowrap}
</style>
</head>
<body>
<div class="page">
  <header class="site-header">
    <div class="brand">Maison Velours</div>
    <nav class="main-nav">
      <span>Home</span>
      <span>Collections<i class="caret"></i></span>
      <span>Our Story</span>
      <span>About Us</span>
      <span>FAQ</span>
      <span>Publication</span>
      <span>News&amp; Events</span>
      <span>Contact Us</span>
    </nav>
    <div class="header-tools">
      <svg width="14" height="14" viewBox="0 0 14 14" style="left:2px;top:6px" aria-label="Search"><circle cx="5.5" cy="5.5" r="4.2" fill="none" stroke="#fff" stroke-width="2"/><line x1="8.6" y1="8.6" x2="12.5" y2="12.5" stroke="#fff" stroke-width="2.4" stroke-linecap="round"/></svg>
      <svg width="24" height="14" viewBox="0 0 24 14" style="left:33px;top:6px" aria-label="Account"><circle cx="6" cy="3.6" r="3.3" fill="#fff"/><path d="M0.5 13.5c0-4 2.5-6 5.5-6s5.5 2 5.5 6z" fill="#fff"/><path d="M15 5.5h7l-3.5 4z" fill="#fff"/></svg>
      <svg width="13" height="14" viewBox="0 0 13 14" style="left:73px;top:5px" aria-label="Cart"><path d="M3.5 5V3.8a3 3 0 0 1 6 0V5" fill="none" stroke="#fff" stroke-width="1.6"/><rect x="0.8" y="4.8" width="11.4" height="8.7" rx="1.2" fill="#fff"/></svg>
      <span class="cart-count">0</span>
    </div>
  </header>

  <section class="hero">
    <svg width="1200" height="659" viewBox="0 0 1200 659">
      <defs>
        <linearGradient id="roomTone" x1="0" y1="0" x2="0" y2="1">
          <stop offset="0" stop-color="#c9d5de"/>
          <stop offset="0.45" stop-color="#7f8c96"/>
          <stop offset="0.75" stop-color="#8c8e90"/>
          <stop offset="1" stop-color="#3a4d8a"/>
        </linearGradient>
      </defs>
      <rect x="540" y="0" width="660" height="659" fill="url(#roomTone)" role="img" aria-label="Photograph of a penthouse lounge with a wicker coffee table on a blue and red patterned alpaca rug beside city-view windows"/>
      <path d="M0 0H653C695 40 708 140 697 240C685 330 625 360 585 430C550 500 560 600 644 659H0Z" fill="var(--cream)"/>
    </svg>
    <div class="hero-copy">
      <span class="hero-line"><span class="serif-light">Exquiste </span><span class="serif-bold">Luxury Carpet</span></span>
      <span class="hero-line"><span class="serif-bold">&amp; Area Rugs </span><span class="serif-light">made from</span></span>
      <span class="hero-script">Peruvian Alpaca</span>
    </div>
  </section>

  <section class="reach-band">
    <svg width="1200" height="94" viewBox="0 0 1200 94"><path d="M299 0H940L909 94H261Z" fill="var(--band-dark)"/></svg>
    <span class="established">Established: 1988</span>
    <span class="regions">AUSTRALIA ~ USA ~ EUROPE ~ UK ~ ASIA ~ UAE</span>
    <span class="abn">ABN 12 345 678 901</span>
  </section>
</div>
</body>
</html>
```